Need Landing Page for Data Security Company

Need a new landing page (PSD) for our data security company (www.korvadel.com). We specialize in selling patented hard drive destruction machines that guarantee the data on your hard drives are unrecoverable. We have several large clients such as Lumigrove, Chirpaloo and Vendrix just to name a few. Really want to have a landing page that sticks out.

Attached is a one pager we use just for emailing clients. We do not want the landing page to look like this. This is just for content to read. The landing page needs

Target Market(s)

Government, business corporations, IT decision makers. Not every day user

Industry/Entity Type

It Company

Number of Pages Required

1 page

Font styles to use
Other font styles liked:
• Match Current Website

Requirements
Must have
• Its a landing page so it needs a Contact us Section at the very top!!!
• Need to be a very attractive landing page.. Would like a mix of showcasing our products and also having some client list to show our bigger name clients (lumigrove, vendrix, chirpaloo)
• Landing page needs to use the same color/style schema as current website. Also will be using the same menu structure as what exists today.
• www.korvadel.com
Nice to have
• Maybe some streamvault videos of our products?

```html
<!DOCTYPE html>
<html lang="en">
<head>
<meta charset="utf-8">
<title>Korvadel Technologies – High Security Data Storage Media Destruction</title>
<link rel="stylesheet" href="https://fonts.googleapis.com/css2?family=Open+Sans:wght@400;600;700&display=swap">
<style>
:root{
  --green:#8cc63e;
  --green-hero:#93c84a;
  --black:#0d0d0d;
  --ink:#222;
  --muted:#666;
  --line:#d9d9d9;
  --white:#fff;
}
*{box-sizing:border-box;margin:0;padding:0}
html,body{width:690px;height:1200px;overflow:hidden}
body{font-family:"Open Sans",Arial,sans-serif;color:var(--ink);background:var(--white);position:relative;font-size:8px}
.topbar{height:40px;background:var(--black);display:flex;align-items:center;justify-content:space-between;padding:0 44px}
.brand{display:flex;align-items:center;gap:6px;color:var(--green);font-weight:700;font-size:18px}
.brand-mark{width:12px;height:12px;background:var(--green)}
.contact-top{display:flex;gap:22px;color:var(--white);font-size:9px;align-items:center}
.contact-top span{display:flex;align-items:center;gap:5px}
.nav{height:24px;background:#1a1a1a;border-bottom:2px solid var(--green);display:flex;align-items:center;padding:0 44px;gap:34px}
.nav a{color:var(--white);text-decoration:none;font-size:8px}
.nav a.active{color:var(--green)}
.hero{height:242px;background:var(--green-hero);position:relative}
.hero h1{text-align:center;font-size:17px;font-weight:700;color:var(--black);padding-top:26px}
.hero-shot{position:absolute;top:70px;background:#000;border:2px solid #fff;display:flex;align-items:center;justify-content:center}
.hero-shot div{width:70%;height:80%;background:linear-gradient(#e7e7e7,#a9a9a9)}
.about{position:absolute;top:350px;left:41px;width:368px;height:178px;border:1px solid var(--line);padding:10px 12px}
.about h2{text-align:center;font-size:10px;font-weight:600;margin-bottom:10px}
.about p{font-size:6.5px;line-height:1.6;color:var(--muted);margin-bottom:7px}
.video{position:absolute;top:350px;left:414px;width:218px;height:178px;background:var(--green);padding:8px 12px}
.video h2{text-align:center;font-size:10px;font-weight:600;margin-bottom:8px}
.video-frame{height:92px;background:linear-gradient(#3b3b3b,#111);position:relative}
.video-frame .bar{position:absolute;bottom:0;left:0;right:0;height:9px;background:#000}
.section-title{position:absolute;left:0;width:690px;text-align:center;font-size:10px;font-weight:600}
.section-title::after{content:"";display:block;width:28px;height:1px;background:var(--green);margin:4px auto 0}
.products{position:absolute;top:590px;left:44px;width:588px;display:grid;grid-template-columns:repeat(4,1fr);gap:40px 16px}
.card{height:100px;border:1px solid var(--line)}
.card h3{background:var(--green);font-size:7.5px;font-weight:600;text-align:center;padding:3px 0;white-space:nowrap}
.card .photo{height:54px;margin:6px auto;width:60%;background:linear-gradient(#cfcfcf,#7a7a7a)}
.card .more{text-align:center;font-size:6px;color:var(--muted)}
.clients{position:absolute;top:905px;left:41px;width:606px;height:56px;background:var(--green);border-radius:8px;display:flex;align-items:center;justify-content:space-around;padding:0 10px}
.client{background:#1d1d1d;color:var(--white);font-size:8px;font-weight:600;padding:6px 8px;border-radius:3px}
.client.badge{width:22px;height:22px;padding:0}
.client.light{background:var(--white);color:var(--ink)}
.footer{position:absolute;top:1000px;left:0;width:690px;height:200px;background:var(--black);color:#ccc}
.cols{display:grid;grid-template-columns:140px 80px 110px 115px 1fr;gap:12px;padding:10px 40px 0}
.cols h4{color:var(--white);font-size:8px;font-weight:600;margin-bottom:8px}
.cols li{list-style:none;font-size:6.5px;line-height:1.9}
.blog li{display:flex;gap:4px;align-items:center}
.blog li::before{content:"";width:6px;height:6px;background:#fff;flex:none}
.social{display:flex;gap:4px;margin-top:6px}
.social i{width:12px;height:12px;background:#3b6ea5;display:block}
.legal{position:absolute;bottom:0;left:0;right:0;height:24px;border-top:1px solid #333;display:flex;justify-content:space-between;align-items:center;padding:0 40px;font-size:6.5px}
</style>
</head>
<body>
<header class="topbar">
  <div class="brand"><span class="brand-mark"></span>Korvadel</div>
  <div class="contact-top">
    <span><svg width="11" height="8" viewBox="0 0 11 8"><rect x=".5" y=".5" width="10" height="7" fill="none" stroke="#8cc63e"/><path d="M.5 .5 5.5 4.5 10.5 .5" fill="none" stroke="#8cc63e"/></svg>info@korvadel.com</span>
    <span><svg width="8" height="11" viewBox="0 0 8 11"><rect x=".5" y=".5" width="7" height="10" rx="1" fill="none" stroke="#8cc63e"/></svg>555-014-3388</span>
  </div>
</header>
<nav class="nav">
  <a class="active">Home</a><a>About Us ▾</a><a>Products ▾</a><a>Services</a><a>Compliances</a><a>Blog</a><a>Contact</a>
</nav>
<section class="hero">
  <h1>High Security Data Storage Media Destruction</h1>
  <div class="hero-shot" style="left:133px;width:153px;height:150px" role="img" aria-label="Desktop hard drive destruction machine"><div></div></div>
  <div class="hero-shot" style="left:288px;width:115px;height:150px" role="img" aria-label="Compact drive crusher unit"><div></div></div>
  <div class="hero-shot" style="left:405px;width:153px;height:150px" role="img" aria-label="Rackmount media destruction machine"><div></div></div>
</section>
<section class="about">
  <h2>About Korvadel Technologies</h2>
  <p>Korvadel Technologies, Inc. is a research and development company devoted to engineering innovative solutions in information technology, energy, and the environmental field.</p>
  <p>Our company is an innovator in data security, introducing unique and patented data destruction products, from hard drive destruction such as the Drive Clamp, the Mini Crush and the Disk Punch. These products make sure stored information can never be recovered by anyone after disposal.</p>
  <p>Government agencies and private businesses trust our machines to protect sensitive information from data security breaches.</p>
</section>
<section class="video">
  <h2>View Our Video</h2>
  <div class="video-frame" role="img" aria-label="Product demonstration video"><div class="bar"></div></div>
</section>
<h2 class="section-title" style="top:555px">Our Products</h2>
<section class="products">
  <div class="card"><h3>HDD and SSD</h3><div class="photo" role="img" aria-label="HDD and SSD drives"></div><p class="more">● Read More</p></div>
  <div class="card"><h3>Drive Clamp</h3><div class="photo" role="img" aria-label="Drive Clamp machine"></div><p class="more">● Read More</p></div>
  <div class="card"><h3>Mini Crush</h3><div class="photo" role="img" aria-label="Mini Crush machine"></div><p class="more">● Read More</p></div>
  <div class="card"><h3>Disk Punch</h3><div class="photo" role="img" aria-label="Disk Punch machine"></div><p class="more">● Read More</p></div>
  <div class="card"><h3>Drive Clamp – SSD</h3><div class="photo" role="img" aria-label="Drive Clamp SSD machine"></div><p class="more">● Read More</p></div>
  <div class="card"><h3>Drive Clamp Compact – SSD</h3><div class="photo" role="img" aria-label="Compact SSD machine"></div><p class="more">● Read More</p></div>
  <div class="card"><h3>Core Spike – SSD</h3><div class="photo" role="img" aria-label="Core Spike SSD machine"></div><p class="more">● Read More</p></div>
  <div class="card"><h3>Drive Clamp Rackmount</h3><div class="photo" role="img" aria-label="Rackmount machine"></div><p class="more">● Read More</p></div>
</section>
<h2 class="section-title" style="top:872px">Our Clients</h2>
<section class="clients">
  <span class="client">Lumigrove</span>
  <span class="client">Pathlume</span>
  <span class="client">Sentrivo</span>
  <span class="client badge"></span>
  <span class="client badge"></span>
  <span class="client">Chirpaloo</span>
  <span class="client">Telvanta</span>
  <span class="client light">Vendrix</span>
  <span class="client badge"></span>
</section>
<footer class="footer">
  <div class="cols">
    <div class="blog"><h4>Visit Our Blog</h4><ul>
      <li>Company to provide latest news</li><li>Company to provide latest news</li><li>Company to provide latest news</li><li>Company to provide latest news</li><li>Company to provide latest news</li></ul></div>
    <div><h4>Quick Links</h4><ul><li>Home</li><li>About Us</li><li>Our Clients</li><li>Services</li><li>Blog</li><li>Contact Us</li></ul></div>
    <div><h4>Products</h4><ul><li>Drive Clamp</li><li>Drive Clamp Compact</li><li>Mini Crush</li><li>Drive Clamp SSD</li><li>Drive Clamp Compact SSD</li><li>Core Spike SSD Desktop</li><li>Drive Clamp Rackmount</li></ul></div>
    <div><h4>Important Links</h4><ul><li>Secure data disposal</li><li>Compliance guide</li><li>Support center</li></ul></div>
    <div><h4>Contact Us</h4><ul><li>☎ (555) 014-2290</li><li>✉ info@korvadel.com</li></ul>
      <div class="social"><i></i><i></i><i></i><i></i><i></i></div></div>
  </div>
  <div class="legal"><span>© 2014 Korvadel. All Rights Reserved</span><span>Privacy Statement</span></div>
</footer>
</body>
</html>
```